Flyer-Design für Immobilienmakler
Meine Vorgaben wurden Umgesetzt aber es wurden auch gute eigene Ideen eingebracht. Änderungswünsche wurden schnell umgesetzt. Danke.
Zielgruppe
Mein Mann und ich sind Immobilienmakler und benötigen immer wieder neue Akquiseflyer.
Diesmal sollen die älteren Immobilienbesitzer angesprochen werde welche ihre Immobilie verkaufen möchten da z.b. die Kinder aus dem Haus sind und etwas kleineres benötigt wird, oder die Wohnung im DG soll verkauft werden weil eine Wohnung im EG sinnvoll wäre.
Frühjahrsaktion: keine Provision für den Verkäufer
Aufgabenstellung
Ca. Din A5, Voder und Rückseite
Als Postkarte. Porto zahlt Empfänger
Der Flyer soll von den Farben her zu den vorherigen passen

```html
<!DOCTYPE html>
<html lang="de">
<head>
<meta charset="utf-8">
<title>Frühjahrsaktion – Postkarte</title>
<link href="https://fonts.googleapis.com/css2?family=Cormorant+Garamond:wght@500&family=Gelasio:wght@400&family=Open+Sans:wght@400&family=Montserrat:wght@500&display=swap" rel="stylesheet">
<style>
  :root {
    --bg: #dcdcdc;
    --white: #ffffff;
    --green-band: rgba(62, 103, 48, 0.9);
    --green-dark: #2f5a24;
    --green-text: #2f5a24;
    --ink: #1c1c1c;
    --benefit-bg: rgba(255, 255, 255, 0.45);
  }
  * { margin: 0; padding: 0; box-sizing: border-box; }
  html, body { width: 1112px; height: 1200px; overflow: hidden; background: var(--bg); }
  .sheet { position: relative; width: 1112px; height: 1200px; }

  .card { position: absolute; top: 102px; width: 502px; height: 354px; background: var(--white); overflow: hidden; }
  .card--front { left: 24px; }
  .card--back { left: 575px; }

  .photo {
    position: absolute; top: 0; height: 354px;
    background:
      radial-gradient(ellipse at 60% 70%, rgba(120,140,60,0.55), transparent 55%),
      linear-gradient(180deg, #f0b820 0%, #d9821c 12%, #8a5a1c 32%, #6b5a22 50%, #7c6a28 62%, #5d6a26 78%, #3f5a1e 100%);
  }
  .card--front .photo { left: 209px; width: 293px; }
  .card--back .photo { left: 0; width: 217px; }

  /* Front */
  .headline-band {
    position: absolute; left: 0; top: 21px; width: 502px; height: 80px;
    background: var(--green-band);
    color: var(--white); font-family: "Cormorant Garamond", serif; font-weight: 500;
    font-size: 24px; line-height: 35px; text-align: center; padding-top: 6px;
    white-space: nowrap;
  }
  .headline-band span { display: block; }
  .headline-band .line-1 { padding-left: 12px; }
  .headline-band .line-2 { padding-right: 10px; }
  .postage { position: absolute; left: 30px; top: 127px; display: flex; align-items: center; gap: 9px; }
  .postage__box {
    width: 36px; height: 43px; border: 1px solid var(--ink);
    font-family: Arial, sans-serif; font-size: 5px; line-height: 7px; text-align: center;
    display: flex; align-items: center; justify-content: center;
  }
  .postage__name { font-family: "Montserrat", sans-serif; font-weight: 500; font-size: 11px; color: var(--ink); }
  .reply-form { position: absolute; left: 15px; top: 194px; width: 174px; list-style: none; }
  .reply-form li {
    display: flex; align-items: baseline; height: 28.4px;
    font-family: "Cormorant Garamond", serif; font-weight: 500; font-size: 11px; color: var(--ink);
  }
  .reply-form li::after { content: ""; flex: 1; border-bottom: 1px dotted var(--ink); margin-left: 1px; }
  .footer-strip { position: absolute; bottom: 0; height: 11px; background: var(--green-dark); }
  .card--front .footer-strip { left: 0; width: 209px; }
  .card--front .footer-strip--over { left: 209px; width: 293px; background: rgba(200,200,190,0.5); }

  /* Back */
  .offer-title {
    position: absolute; left: 7px; top: 34px; width: 225px; height: 28px;
    background: var(--green-dark); color: var(--white);
    font-family: "Cormorant Garamond", serif; font-weight: 500; font-size: 20px; line-height: 28px;
    padding-left: 17px; white-space: nowrap; overflow: hidden;
  }
  .benefits { position: absolute; left: 17px; top: 89px; list-style: none; }
  .benefits li {
    position: relative; width: 182px; height: 25px; margin-bottom: 10px;
    background: var(--benefit-bg); color: var(--white);
    font-family: "Gelasio", serif; font-weight: 400; font-size: 8.6px; line-height: 11.5px;
    padding: 1px 0 0 12px; white-space: nowrap; overflow: hidden;
  }
  .benefits li::before {
    content: ""; position: absolute; left: 1px; top: 8px;
    border-left: 7px solid var(--white); border-top: 4.5px solid transparent; border-bottom: 4.5px solid transparent;
  }
  .brand { position: absolute; left: 274px; top: 26px; width: 176px; text-align: center; color: var(--green-text); font-family: "Gelasio", serif; }
  .brand__mark { display: inline-block; width: 9px; height: 9px; background: var(--green-text); margin-bottom: 3px; }
  .brand__name { display: block; font-size: 17px; line-height: 22px; }
  .brand__sub { display: block; font-size: 7px; letter-spacing: 3px; line-height: 10px; margin-top: 2px; }
  .intro {
    position: absolute; left: 274px; top: 97px; width: 176px;
    font-family: "Open Sans", sans-serif; font-size: 7.6px; line-height: 12.6px; color: var(--ink);
    text-align: justify; hyphens: auto;
  }
  .contact {
    position: absolute; top: 291px; font-family: "Gelasio", serif; font-size: 8.8px; line-height: 12px;
    color: var(--green-text); white-space: nowrap;
  }
  .contact--phone { left: 232px; }
  .contact--address { left: 357px; }
  .card--back .footer-strip {
    left: 217px; width: 285px; height: 14px; color: var(--white);
    font-family: "Gelasio", serif; font-size: 10px; line-height: 14px; text-align: center; white-space: nowrap;
  }
</style>
</head>
<body>
<main class="sheet">

  <section class="card card--front" aria-label="Vorderseite">
    <div class="photo" role="img" aria-label="Foto: älteres Paar sitzt umarmt im Gras am See im Abendlicht"></div>
    <h1 class="headline-band">
      <span class="line-1">Frühjahrsaktion:</span>
      <span class="line-2">keine Provision für den Verkäufer</span>
    </h1>
    <div class="postage">
      <div class="postage__box">Entgelt<br>zahlt<br>Empfänger</div>
      <span class="postage__name">Briefwerk</span>
    </div>
    <ul class="reply-form">
      <li>Name:</li>
      <li>Telefon:</li>
      <li>Straße:</li>
      <li>PLZ/ORT:</li>
      <li>Email:</li>
    </ul>
    <div class="footer-strip"></div>
    <div class="footer-strip footer-strip--over"></div>
  </section>

  <section class="card card--back" aria-label="Rückseite">
    <div class="photo" role="img" aria-label="Foto: älteres Paar sitzt umarmt im Gras am See im Abendlicht"></div>
    <h2 class="offer-title">Lorem ipsum dolor stetuer</h2>
    <ul class="benefits">
      <li>lorem ipsum dolor sit amet,<br>adipiscing elit, sed diam nonummy</li>
      <li>lorem ipsum dolor sit amet,<br>adipiscing elit, sed diam nonummy</li>
      <li>lorem ipsum dolor sit amet,<br>adipiscing elit, sed diam nonummy</li>
    </ul>
    <div class="brand">
      <span class="brand__mark"></span>
      <span class="brand__name">Marlene Brandt</span>
      <span class="brand__sub">IMMOBILIEN</span>
    </div>
    <p class="intro">Lorem ipsum dolor sit amet, consectetuer adipiscing elit, sed diam nonummy nibh euismod tincidunt ut laoreet dolore magna aliquam erat volutpat. Ut wisi enim ad minim veniam, quis nostrud exerci tation ullamcorper suscipit lobortis nisl ut aliquip ex ea commodo consequat. Duis autem vel eum iriure dolor in hendrerit in vulputate velit esse molestie consequat, vel illum dolore eu feugiat nulla facilisis at. Lorem ipsum dolor sit amet, consectetuer adipiscing elit, sed diam nonummy nibh euismod.</p>
    <p class="contact contact--phone">Telefon: 08221-437 20 91<br>info@brandt-immobilien.de</p>
    <p class="contact contact--address">Am Mühlgraben 7, beim Rathaus<br>im Zentrum von Lindenau</p>
    <div class="footer-strip">www.brandt-immobilien-lindenau.de</div>
  </section>

</main>
</body>
</html>
```